Web app UI design

This web app has been built and the UI needs a refresh.

Attached are the pages which need the refresh.

The web app is for a cyber security product/service and customers are inputting their details.

```html
<!DOCTYPE html>
<html lang="en">
<head>
<meta charset="UTF-8">
<title>Subscription</title>
<link href="https://fonts.googleapis.com/css2?family=Inter:wght@400;500;600;700;800&display=swap" rel="stylesheet">
<style>
  :root {
    --bg: #1d2029;
    --card: #20232e;
    --divider: #272a35;
    --blue: #2d68e8;
    --white: #ffffff;
    --text: #e6e8ee;
    --muted: #8c909c;
    --muted-blue: #9db8f2;
    --icon: #7d818d;
    --outline: #363a46;
    --online: #22d65e;
    --avatar: #6b5448;
  }
  * { box-sizing: border-box; margin: 0; padding: 0; }
  html, body { width: 1200px; height: 716px; overflow: hidden; background: var(--bg); }
  body { font-family: "Inter", sans-serif; color: var(--text); position: relative; }

  .sidebar {
    position: absolute; left: 0; top: 0; width: 101px; height: 716px;
    border-right: 1px solid var(--divider);
  }
  .menu-toggle { position: absolute; left: 38px; top: 39px; }
  .nav-item {
    position: absolute; left: 25px; width: 53px; height: 53px;
    display: flex; align-items: center; justify-content: center; border-radius: 8px;
  }
  .nav-item.is-active { background: var(--blue); }
  .avatar {
    position: absolute; left: 35px; top: 635px; width: 34px; height: 34px;
    border-radius: 50%; background: radial-gradient(circle at 50% 40%, #a07d66, var(--avatar));
  }
  .status-dot {
    position: absolute; left: 63px; top: 640px; width: 9px; height: 9px;
    border-radius: 50%; background: var(--online);
  }

  .page-title {
    position: absolute; left: 145px; top: 32px; font-size: 16px; font-weight: 400;
    color: #b7bac3; letter-spacing: 0.2px;
  }

  .plan {
    position: absolute; top: 135px; width: 239px; height: 382px;
    border-radius: 16px; background: var(--card);
  }
  .plan--bronze { left: 249px; }
  .plan--silver { left: 525px; background: var(--blue); }
  .plan--gold { left: 802px; }

  .plan-name {
    position: absolute; left: 32px; top: 27px; font-size: 31.5px; font-weight: 700; color: var(--white);
  }
  .features { position: absolute; left: 32px; top: 90px; list-style: none; width: 195px; }
  .features li {
    position: relative; padding-left: 19px; font-size: 12px; line-height: 16px;
    color: var(--white); margin-bottom: 11px;
  }
  .features li svg { position: absolute; left: 0; top: 4px; }
  .features strong { font-weight: 600; }

  .price { position: absolute; left: 32px; top: 223px; font-size: 32px; font-weight: 700; color: var(--white); }
  .price-ask {
    position: absolute; left: 32px; top: 227px; font-size: 19px; line-height: 22px;
    font-weight: 700; color: var(--white);
  }
  .period { position: absolute; left: 32px; font-size: 13px; color: var(--muted); }
  .plan--bronze .period { top: 267px; }
  .plan--silver .period, .plan--gold .period { top: 279px; }
  .plan--silver .period { color: var(--muted-blue); }

  .plan-button {
    position: absolute; left: 14px; top: 317px; width: 207px; height: 48px; border-radius: 9px;
    display: flex; align-items: center; justify-content: center; font-family: inherit;
    font-size: 16px; font-weight: 600; border: none;
  }
  .plan-button--subscribed { background: transparent; border: 1px solid var(--outline); color: #4d515d; font-weight: 400; }
  .plan-button--light { background: var(--white); color: var(--blue); }
  .plan-button--primary { background: var(--blue); color: var(--white); }

  .manage-button {
    position: absolute; left: 542px; top: 620px; width: 206px; height: 48px; border-radius: 9px;
    border: 1px solid var(--blue); background: transparent; color: var(--blue);
    font-family: inherit; font-size: 16px; font-weight: 400;
    display: flex; align-items: center; justify-content: center;
  }
</style>
</head>
<body>
  <aside class="sidebar">
    <svg class="menu-toggle" width="29" height="10" viewBox="0 0 29 10" fill="none" stroke="#e6e8ee" stroke-width="1.6" stroke-linecap="round">
      <line x1="1" y1="1" x2="28" y2="1"/><line x1="1" y1="9" x2="16" y2="9"/>
    </svg>
    <div class="nav-item" style="top:90px">
      <svg width="28" height="28" viewBox="0 0 28 28" fill="none" stroke="var(--icon)" stroke-width="1.6" stroke-linejoin="round">
        <path d="M4 12 14 3l10 9v12a1 1 0 0 1-1 1h-5v-7h-8v7H5a1 1 0 0 1-1-1z"/>
      </svg>
    </div>
    <div class="nav-item" style="top:168px">
      <svg width="28" height="28" viewBox="0 0 28 28" fill="none" stroke="var(--icon)" stroke-width="1.6" stroke-linecap="round">
        <circle cx="12" cy="8" r="5"/><path d="M3 25c0-5 4-8 9-8 2 0 3 .3 4 .8M3 25h11"/><path d="m18 25 1-4 5-5 2 2-5 5z"/>
      </svg>
    </div>
    <div class="nav-item is-active" style="top:245px">
      <svg width="26" height="26" viewBox="0 0 26 26" fill="none" stroke="#fff" stroke-width="1.6" stroke-linecap="round" stroke-linejoin="round">
        <rect x="3" y="3" width="16" height="18" rx="3"/><path d="M10 21v-9a1.5 1.5 0 0 1 3 0v5M13 15a1.5 1.5 0 0 1 3 0v2M16 16a1.5 1.5 0 0 1 3 0v3c0 3-2 5-5 5h-1c-2 0-3-1-4-2l-2-3"/>
      </svg>
    </div>
    <div class="nav-item" style="top:323px">
      <svg width="28" height="28" viewBox="0 0 28 28" fill="none" stroke="var(--icon)" stroke-width="1.6" stroke-linecap="round" stroke-linejoin="round">
        <circle cx="12" cy="8" r="5"/><path d="M3 25c0-5 4-8 9-8 1.5 0 3 .3 4 .8M3 25h10"/><path d="m17 22 3 3 6-6"/>
      </svg>
    </div>
    <div class="avatar" role="img" aria-label="User profile photo"></div>
    <span class="status-dot"></span>
  </aside>

  <h1 class="page-title">Subscription</h1>

  <section class="plan plan--bronze">
    <h2 class="plan-name">Bronze</h2>
    <ul class="features">
      <li><svg width="10" height="8" viewBox="0 0 10 8" fill="none" stroke="#fff" stroke-width="1.8"><path d="m1 4 3 3 5-6"/></svg>Access to<br><strong>verification system</strong></li>
      <li><svg width="10" height="8" viewBox="0 0 10 8" fill="none" stroke="#fff" stroke-width="1.8"><path d="m1 4 3 3 5-6"/></svg>Use of Veridoxa logo<br>and material on <strong>website<br>and document</strong></li>
      <li><svg width="10" height="8" viewBox="0 0 10 8" fill="none" stroke="#fff" stroke-width="1.8"><path d="m1 4 3 3 5-6"/></svg>Other <strong>perks</strong></li>
    </ul>
    <p class="price">$85</p>
    <p class="period">Monthly</p>
    <button class="plan-button plan-button--subscribed">Subscribed</button>
  </section>

  <section class="plan plan--silver">
    <h2 class="plan-name">Silver</h2>
    <ul class="features">
      <li><svg width="10" height="8" viewBox="0 0 10 8" fill="none" stroke="#fff" stroke-width="1.8"><path d="m1 4 3 3 5-6"/></svg><strong>Bronze</strong> plan+</li>
      <li><svg width="10" height="8" viewBox="0 0 10 8" fill="none" stroke="#fff" stroke-width="1.8"><path d="m1 4 3 3 5-6"/></svg><strong>Cyber insurance</strong><br>in case of event</li>
      <li><svg width="10" height="8" viewBox="0 0 10 8" fill="none" stroke="#fff" stroke-width="1.8"><path d="m1 4 3 3 5-6"/></svg><strong>Dedicated support</strong><br>to remediate events</li>
    </ul>
    <p class="price-ask">Contact us<br>for price</p>
    <p class="period">Monthly</p>
    <button class="plan-button plan-button--light">Contact</button>
  </section>

  <section class="plan plan--gold">
    <h2 class="plan-name">Gold</h2>
    <ul class="features">
      <li><svg width="10" height="8" viewBox="0 0 10 8" fill="none" stroke="#fff" stroke-width="1.8"><path d="m1 4 3 3 5-6"/></svg><strong>Silver</strong> plan+</li>
      <li><svg width="10" height="8" viewBox="0 0 10 8" fill="none" stroke="#fff" stroke-width="1.8"><path d="m1 4 3 3 5-6"/></svg><strong>Cybersecurity</strong><br>expert on retainer</li>
      <li><svg width="10" height="8" viewBox="0 0 10 8" fill="none" stroke="#fff" stroke-width="1.8"><path d="m1 4 3 3 5-6"/></svg>System <strong>reviews</strong></li>
      <li><svg width="10" height="8" viewBox="0 0 10 8" fill="none" stroke="#fff" stroke-width="1.8"><path d="m1 4 3 3 5-6"/></svg><strong>Phone</strong> consultations</li>
    </ul>
    <p class="price-ask">Contact us<br>for price</p>
    <p class="period">Monthly</p>
    <button class="plan-button plan-button--primary">Contact</button>
  </section>

  <button class="manage-button">Manage Subsription</button>
</body>
</html>
```